Power Generation Company needs a stationary design

We need a design for our letter envelope, A4 Envelope and letterhead. Our company name is BRIMVolt which i attached here sample our our call card. We are based in the Philippines and is into the Power Generation business. We own power facilities like Hydropower plant, Solar Power Plant, Diesel Power Plant, Gas Turbine Power Plant. We sell our power to various electric distribution companies, factories and office buildings.

Target Market(s)

Electric Distribution Companies and Factories

Industry/Entity Type

It Company

Colors
ec1f27

Requirements
Must have
• Logo and company name
Nice to have
• No specific
Should not have
• No specific

```html
<!DOCTYPE html>
<html lang="en">
<head>
<meta charset="utf-8">
<title>BRIMVolt Stationery</title>
<link href="https://fonts.googleapis.com/css2?family=Quicksand:wght@600&family=Roboto:wght@400;500&display=swap" rel="stylesheet">
<style>
  :root{
    --brand-red:#ec1f27;
    --paper:#ffffff;
    --backdrop:#e9e6e2;
    --ink-light:#ffffff;
    --ink-dark:#3a3a3a;
  }
  *{box-sizing:border-box;margin:0;padding:0}
  html,body{width:1200px;height:1200px;overflow:hidden}
  body{background:var(--backdrop);position:relative;font-family:"Roboto",sans-serif}
  .sheet{position:absolute;background:var(--paper);overflow:hidden;box-shadow:0 4px 14px rgba(0,0,0,.18)}
  .wordmark{position:absolute;display:flex;align-items:center;gap:.3em;color:var(--brand-red);font-family:"Roboto",sans-serif;font-weight:400;letter-spacing:.04em;white-space:nowrap}
  .wordmark .dot{width:.75em;height:.75em;border:1.5px solid currentColor;border-radius:50%}
  .wordmark.on-red{color:var(--ink-light)}
  .address{position:absolute;color:var(--ink-dark);line-height:1.45;font-style:normal;white-space:nowrap}
  .address .company{color:var(--brand-red);font-weight:500}
  .contacts{position:absolute;color:var(--ink-light);list-style:none;white-space:nowrap}
  .contacts li{display:flex;gap:.7em}
  .contacts b{font-weight:400;width:.8em}
  .band{position:absolute;left:0;top:0}

  /* Letterhead */
  .letterhead{left:58px;top:132px;width:606px;height:856px}
  .letterhead .wordmark{left:39px;top:38px;font-size:28px}
  .letterhead .address{left:436px;top:30px;font-size:8.4px}
  .letterhead .contacts{left:24px;top:768px;font-size:12px;line-height:14.6px}

  /* Envelope */
  .envelope{left:737px;top:95px;width:365px;height:580px;border-radius:14px 14px 0 0}
  .envelope .flap{position:absolute;left:0;top:0;width:100%;height:53px;background:var(--brand-red)}
  .envelope .wordmark{left:20px;top:74px;font-size:15px}
  .envelope .address{left:229px;top:72px;font-size:6.4px}
  .envelope .contacts{left:12px;top:529px;font-size:6.6px;line-height:9px;font-weight:500}

  /* Business card front */
  .card-front{left:766px;top:740px;width:283px;height:161px}
  .card-front .holder{position:absolute;left:16px;top:33px;color:var(--ink-light);font-family:"Quicksand",sans-serif;font-weight:600;font-size:14px}
  .card-front .address{left:16px;top:59px;font-size:5.6px;color:var(--ink-light)}
  .card-front .address .company{color:var(--ink-light)}
  .card-front .contacts{left:16px;top:106px;font-size:5.4px;line-height:8px;font-weight:500}
  .card-front .wordmark{left:182px;top:58px;font-size:13px}

  /* Business card back */
  .card-back{left:764px;top:942px;width:282px;height:161px;background:var(--brand-red)}
  .card-back .wordmark{left:50%;top:50%;transform:translate(-50%,-50%);font-size:22px}
</style>
</head>
<body>

<section class="sheet letterhead" aria-label="Letterhead">
  <div class="wordmark"><span class="dot"></span>BRIMVolt</div>
  <address class="address">
    <div class="company">BRIMVOLT INC.</div>
    14 Riverside Energy Center,<br>
    88 Narra St., Lakeview Business Park,<br>
    Santa Rosa, Laguna, 4026 Philippines
  </address>
  <svg class="band" width="606" height="856" viewBox="0 0 606 856" aria-hidden="true">
    <polygon points="0,704 606,826 606,856 0,856" fill="var(--brand-red)"/>
  </svg>
  <ul class="contacts">
    <li><b>T</b>+632-555-0140</li>
    <li><b>F</b>+632-555-0141</li>
    <li><b>M</b>+63-900-555-0192</li>
    <li><b>E</b>leomarquez@brimvolt-net.com</li>
  </ul>
</section>

<section class="sheet envelope" aria-label="Envelope">
  <div class="flap"></div>
  <div class="wordmark"><span class="dot"></span>BRIMVolt</div>
  <address class="address">
    <div class="company">BRIMVOLT INC.</div>
    14 Riverside Energy Center,<br>
    88 Narra St., Lakeview Business Park,<br>
    Santa Rosa, Laguna, 4026 Philippines
  </address>
  <svg class="band" width="365" height="580" viewBox="0 0 365 580" aria-hidden="true">
    <polygon points="0,500 365,566 365,580 0,580" fill="var(--brand-red)"/>
  </svg>
  <ul class="contacts">
    <li><b>T</b>+632-555-0140</li>
    <li><b>F</b>+632-555-0141</li>
    <li><b>M</b>+63-900-555-0192</li>
    <li><b>E</b>leomarquez@brimvolt-net.com</li>
  </ul>
</section>

<section class="sheet card-front" aria-label="Business card front">
  <svg class="band" width="283" height="161" viewBox="0 0 283 161" aria-hidden="true">
    <polygon points="0,0 112,0 232,161 0,161" fill="var(--brand-red)"/>
  </svg>
  <div class="holder">Leo Marquez</div>
  <address class="address">
    <div class="company">BRIMVOLT INC.</div>
    14 Riverside Energy Center,<br>
    88 Narra St., Lakeview Business Park,<br>
    Santa Rosa, Laguna, 4026 Philippines
  </address>
  <ul class="contacts">
    <li><b>T</b>+632-555-0140</li>
    <li><b>F</b>+632-555-0141</li>
    <li><b>M</b>+63-900-555-0192</li>
    <li><b>E</b>leomarquez@brimvolt-net.com</li>
  </ul>
  <div class="wordmark"><span class="dot"></span>BRIMVolt</div>
</section>

<section class="sheet card-back" aria-label="Business card back">
  <div class="wordmark on-red"><span class="dot"></span>BRIMVolt</div>
</section>

</body>
</html>
```